Business card and company stationary - Corvane Cleaning Ltd

1. Who are we and who are our customers?

o We are a relatively new cleaning company, established December 2008. We are a small company. We have 24 staff and we offer domestic and commercial cleaning services.
o We both (me and my wife) have been working for many years in the cleaning industry. We worked for some of the biggest and best cleaning companies in UK. We’ve been operatives, supervisors and managers.
o Inevitably after so many years of working for someone else, we decided to start our own business.
o Our domestic customers are middle class families and busy professionals. We’ve got some commercial customers, mainly offices.
o We are growing steadily.

2. What do we do? What are our services?

o Cleaning. We’ve got range of services - not to many but still can be daunting and confusing for some.
o Generally we’ve got domestic and commercial clients. The approach to the domestic cleaning customers is different to the commercial. In the way we want to say that it is cleaning that we do, but we acknowledge the environment and we appreciate the personal circumstances and requirements that are present. We do care, we listen and we try to work out the best possible way to complete our work.
o Mainly we get our work through referrals

3. What do we want with our stationery ?

o To place and maintain our message and reach out to people and organisations
o We want to advertise, communicate and sale.
o We are going to sell services.
o Increase membership, loyalty and support.

We are after business card design, headed letter and compliment slip.
We would like the headed letter to be created in formats suitable for :
- printing format
- also for use in our daily correspondence via e mail with clients and staff in a easy to edit and write format

The website we have is still under contraction and the domain is corvanecleaning.example

Target Market(s)

Families, individuals, businesses.

Industry/Entity Type

Cleaning Service

Contact Information for Business Card

FRONT :
Company Name - Corvane Cleaning Ltd
Company address - 41 Pelbury Rd, Pelbury, Essex, RM14 7QT
Name - Mrs. Teodora Vasilkova - Tedi
Title - Managing Director
Company phone - 020 8837 2591
E mail - tedi.vasilkova@corvanecleaning.example

BACK :

Company website - corvanecleaning.example
E mail - enquiries@corvanecleaning.example

Font styles to use
Serif

Requirements
Must have
• The above items and company logo...maybe at the back. But I'm free for any suggestions.

```html
<!DOCTYPE html>
<html lang="en">
<head>
<meta charset="utf-8">
<title>Corvane Cleaning Ltd – Stationery</title>
<link rel="stylesheet" href="https://fonts.googleapis.com/css2?family=PT+Serif:wght@400;700&display=swap">
<style>
  :root {
    --bg: #e9eaeb;
    --paper: #ffffff;
    --ink: #121212;
    --body: #555555;
    --accent: #2aa3d2;
    --band: #0d0d0d;
    --shadow: 0 6px 18px rgba(0,0,0,.12);
  }
  * { box-sizing: border-box; margin: 0; padding: 0; }
  html, body { width: 1200px; height: 2660px; overflow: hidden; }
  body {
    position: relative;
    background: var(--bg);
    font-family: "PT Serif", Georgia, serif;
    color: var(--ink);
  }
  .piece {
    position: absolute;
    background: var(--paper);
    box-shadow: var(--shadow);
    overflow: hidden;
  }
  .band { position: absolute; left: 0; right: 0; background: var(--band); }
  .badge {
    position: absolute;
    border-radius: 50%;
    background: var(--paper);
    border: 3px solid var(--band);
    display: flex; align-items: center; justify-content: center;
    text-align: center;
    transform: translate(-50%, -50%);
  }
  .brand-name {
    font-weight: 700;
    color: var(--accent);
    text-transform: uppercase;
    letter-spacing: .04em;
    line-height: 1.1;
  }
  .lockup { position: absolute; display: flex; flex-direction: column; align-items: center; text-align: center; }
  .lockup-circle { border-radius: 50%; border: 3px solid var(--ink); }

  /* Headed letter */
  .letterhead { left: 60px; top: 80px; width: 560px; height: 792px; }
  .letterhead .lockup { left: 0; right: 0; top: 36px; gap: 8px; }
  .letterhead .lockup-circle { width: 42px; height: 42px; }
  .letterhead .brand-name { font-size: 13px; }
  .letter-body {
    position: absolute; left: 62px; right: 62px; top: 150px;
    font-size: 8.6px; line-height: 1.75; color: var(--body);
  }
  .letter-body p + p { margin-top: 12px; }
  .letter-footer {
    position: absolute; left: 36px; right: 36px; top: 708px;
    display: flex; justify-content: space-between;
    font-size: 6.5px; color: var(--body);
  }
  .letter-footer .label { color: var(--accent); font-weight: 700; }
  .letterhead .band { top: 740px; height: 20px; }
  .letterhead .badge { left: 280px; top: 750px; width: 56px; height: 56px; }
  .letterhead .badge .brand-name { font-size: 6.5px; }

  /* Business card back */
  .card-back { left: 640px; top: 80px; width: 500px; height: 286px; }
  .card-back .band { top: 100px; height: 56px; }
  .card-back .badge { left: 170px; top: 128px; width: 100px; height: 100px; }
  .card-back .badge .brand-name { font-size: 9.5px; }
  .web { position: absolute; font-size: 13px; color: var(--ink); letter-spacing: .01em; }
  .card-back .web { left: 100px; top: 196px; }

  /* Business card front */
  .card-front { left: 640px; top: 406px; width: 500px; height: 286px; }
  .card-front .lockup { left: 22px; top: 70px; width: 170px; gap: 10px; }
  .card-front .lockup-circle { width: 62px; height: 62px; }
  .card-front .brand-name { font-size: 14px; }
  .contact { position: absolute; font-size: 9.5px; line-height: 1.65; color: var(--body); white-space: nowrap; }
  .contact .person { font-size: 16px; font-weight: 700; color: var(--ink); line-height: 1.2; }
  .contact .role { font-size: 9.5px; color: var(--ink); margin-bottom: 8px; }
  .contact .label { color: var(--accent); font-weight: 700; display: inline-block; width: 40px; }
  .card-front .contact { left: 212px; top: 70px; }

  /* Compliment slip */
  .slip { left: 60px; top: 952px; width: 1080px; height: 510px; }
  .slip .lockup { left: 50px; top: 60px; width: 200px; gap: 10px; }
  .slip .lockup-circle { width: 70px; height: 70px; }
  .slip .brand-name { font-size: 16px; }
  .slip .contact { left: 290px; top: 110px; font-size: 11px; }
  .slip .contact .person { font-size: 19px; }
  .slip .contact .role { font-size: 11px; }
  .slip .contact .label { width: 46px; }
  .compliments {
    position: absolute; right: 80px; top: 230px;
    font-size: 28px; font-weight: 700; color: var(--ink);
  }
  .slip .band { bottom: 70px; height: 58px; }
  .slip .badge { left: 540px; top: 411px; width: 112px; height: 112px; }
  .slip .badge .brand-name { font-size: 10.5px; }

  /* Presentation folder */
  .folder { left: 280px; top: 1560px; width: 640px; height: 905px; }
  .folder .band { top: 240px; height: 82px; }
  .folder .badge { left: 320px; top: 281px; width: 176px; height: 176px; border-width: 4px; }
  .folder .badge .brand-name { font-size: 15px; }
  .folder .web { left: 0; right: 0; top: 392px; text-align: center; font-size: 18px; }
</style>
</head>
<body>

  <section class="piece letterhead" aria-label="Headed letter">
    <div class="lockup">
      <span class="lockup-circle"></span>
      <span class="brand-name">Corvane Cleaning Ltd</span>
    </div>
    <div class="letter-body">
      <p>Thank you for choosing us for your home and office cleaning. This letter sets out the details of the service we agreed, the dates of each visit and the names of the team who will look after your rooms.</p>
      <p>Our staff are trained, insured and checked, and each visit follows a written plan made for your space. We bring our own tools and products, and we are glad to use yours if you prefer. Please tell us about pets, alarms, keys or rooms that need special care.</p>
      <p>If your plans change, call the office at least two days before the visit and we will move it to a time that suits you. Invoices are sent at the end of each month and may be paid by bank transfer or card.</p>
      <p>We value your feedback. After the first month we will ask how we are doing, and we will act on what you tell us. Thank you again for your trust; we look forward to working with you.</p>
    </div>
    <div class="letter-footer">
      <span>41 Pelbury Rd, Pelbury, Essex, RM14 7QT &nbsp;<span class="label">Phone</span> 020 8837 2591</span>
      <span><span class="label">Email</span> enquiries@corvanecleaning.example &nbsp; corvanecleaning.example</span>
    </div>
    <div class="band"></div>
    <div class="badge"><span class="brand-name">Corvane</span></div>
  </section>

  <section class="piece card-back" aria-label="Business card back">
    <div class="band"></div>
    <div class="badge"><span class="brand-name">Corvane<br>Cleaning Ltd</span></div>
    <p class="web">www.corvanecleaning.example</p>
  </section>

  <section class="piece card-front" aria-label="Business card front">
    <div class="lockup">
      <span class="lockup-circle"></span>
      <span class="brand-name">Corvane<br>Cleaning Ltd</span>
    </div>
    <div class="contact">
      <p class="person">Teodora Vasilkova</p>
      <p class="role">Managing Director</p>
      <p>41 Pelbury Rd, Pelbury, Essex, RM14 7QT</p>
      <p><span class="label">Phone</span>020 8837 2591</p>
      <p><span class="label">Email</span>tedi.vasilkova@corvanecleaning.example</p>
      <p>www.corvanecleaning.example</p>
    </div>
  </section>

  <section class="piece slip" aria-label="Compliment slip">
    <div class="lockup">
      <span class="lockup-circle"></span>
      <span class="brand-name">Corvane<br>Cleaning Ltd</span>
    </div>
    <div class="contact">
      <p class="person">Teodora Vasilkova</p>
      <p class="role">Managing Director</p>
      <p>41 Pelbury Rd, Pelbury, Essex, RM14 7QT</p>
      <p><span class="label">Phone</span>020 8837 2591</p>
      <p><span class="label">Email</span>tedi.vasilkova@corvanecleaning.example</p>
      <p>www.corvanecleaning.example</p>
    </div>
    <p class="compliments">With Compliments</p>
    <div class="band"></div>
    <div class="badge"><span class="brand-name">Corvane<br>Cleaning Ltd</span></div>
  </section>

  <section class="piece folder" aria-label="Presentation folder">
    <div class="band"></div>
    <div class="badge"><span class="brand-name">Corvane<br>Cleaning Ltd</span></div>
    <p class="web">www.corvanecleaning.example</p>
  </section>

</body>
</html>
```